PowerPoint design of key models

We recently had a new PPT template created which we are very happy with. Now we want to have some of our key models on various pages in PPT to be reformatted and redesigned to match the other graphics of the new PT template. Can you please redesign the models and graphics so they have the same look and feel as the new template. I have included both files for you to work with. Thank you.

```html
<!DOCTYPE html>
<html lang="en">
<head>
<meta charset="utf-8">
<title>Key Models</title>
<link href="https://fonts.googleapis.com/css2?family=Montserrat:wght@600;700&display=swap" rel="stylesheet">
<style>
  :root {
    --backdrop: #5b5b5b;
    --panel: #ffffff;
    --ink: #111111;
    --magenta: #c9238f;
    --violet: #a335e5;
    --blue: #1a94e8;
    --cyan: #12d4e0;
    --navy: #001f4d;
  }
  html, body {
    margin: 0;
    padding: 0;
    width: 1200px;
    height: 2691px;
    overflow: hidden;
    background: var(--backdrop);
  }
  .board {
    position: relative;
    width: 1200px;
    height: 2691px;
    font-family: "Montserrat", sans-serif;
  }
  .board svg {
    position: absolute;
    left: 0;
    top: 0;
    width: 1200px;
    height: 2691px;
  }
  .label { font-family: "Montserrat", sans-serif; font-weight: 700; fill: var(--ink); }
  .bar-text { font-family: "Montserrat", sans-serif; font-weight: 700; fill: #fff; font-size: 23px; }
  .icon { fill: none; stroke: #fff; stroke-width: 2; stroke-linecap: round; stroke-linejoin: round; }
  .arrow { fill: none; stroke: var(--ink); stroke-width: 3.5; stroke-linecap: round; stroke-linejoin: round; }
</style>
</head>
<body>
<div class="board">
<svg viewBox="0 0 1149 2576" xmlns="http://www.w3.org/2000/svg">
  <defs>
    <filter id="soft-shadow" x="-40%" y="-40%" width="180%" height="180%">
      <feDropShadow dx="0" dy="6" stdDeviation="10" flood-color="#000" flood-opacity="0.14"/>
    </filter>
    <filter id="wide-shadow" x="-60%" y="-60%" width="220%" height="220%">
      <feDropShadow dx="0" dy="10" stdDeviation="22" flood-color="#000" flood-opacity="0.12"/>
    </filter>
    <linearGradient id="ring-main" x1="0" y1="0" x2="1" y2="0">
      <stop offset="0" stop-color="#2ec799"/>
      <stop offset="0.4" stop-color="#b070d8"/>
      <stop offset="0.75" stop-color="#e8584f"/>
      <stop offset="1" stop-color="#f7a12c"/>
    </linearGradient>
    <linearGradient id="ring-core" x1="0" y1="0" x2="1" y2="1">
      <stop offset="0" stop-color="#2ec7c7"/>
      <stop offset="0.45" stop-color="#9a7ae8"/>
      <stop offset="1" stop-color="#f7a12c"/>
    </linearGradient>
    <linearGradient id="node-task" x1="0" y1="0" x2="1" y2="1">
      <stop offset="0" stop-color="#e0468a"/>
      <stop offset="1" stop-color="#c074e0"/>
    </linearGradient>
    <linearGradient id="node-individual" x1="0" y1="1" x2="1" y2="0">
      <stop offset="0" stop-color="#e0555e"/>
      <stop offset="1" stop-color="#f9ab2a"/>
    </linearGradient>
    <linearGradient id="node-team" x1="0" y1="0" x2="1" y2="1">
      <stop offset="0" stop-color="#24c796"/>
      <stop offset="1" stop-color="#c070e0"/>
    </linearGradient>
    <linearGradient id="disc-magenta" x1="0" y1="0" x2="1" y2="1">
      <stop offset="0" stop-color="#e045a8"/>
      <stop offset="1" stop-color="#b81e84"/>
    </linearGradient>
    <linearGradient id="disc-violet" x1="0" y1="0" x2="1" y2="1">
      <stop offset="0" stop-color="#b040ec"/>
      <stop offset="1" stop-color="#8a2ad0"/>
    </linearGradient>
    <linearGradient id="disc-blue" x1="0" y1="0" x2="1" y2="1">
      <stop offset="0" stop-color="#2aa6f0"/>
      <stop offset="1" stop-color="#1478d6"/>
    </linearGradient>
    <linearGradient id="disc-cyan" x1="0" y1="0" x2="1" y2="1">
      <stop offset="0" stop-color="#22e2ea"/>
      <stop offset="1" stop-color="#0cc0d4"/>
    </linearGradient>
    <radialGradient id="hub-fill" cx="0.5" cy="0.5" r="0.5">
      <stop offset="0" stop-color="#ffffff"/>
      <stop offset="1" stop-color="#f1f1f1"/>
    </radialGradient>
  </defs>

  <!-- Panel 1: Task / Team / Individual -->
  <g class="panel-model">
    <rect x="62" y="68" width="1025" height="777" fill="var(--panel)"/>
    <circle cx="528" cy="438" r="243" fill="none" stroke="url(#ring-main)" stroke-width="18"/>

    <path class="connector-hub" filter="url(#soft-shadow)" fill="#fff"
      d="M410 300
         L470 300
         C505 340 585 320 640 380
         C665 408 690 420 720 430
         L730 500
         C690 500 660 490 620 500
         C560 515 505 510 470 560
         L400 560
         C440 510 455 470 450 433
         C445 395 420 360 410 300 Z"/>
    <circle cx="528" cy="433" r="96" fill="#fff"/>
    <circle cx="528" cy="433" r="78" fill="#fff" stroke="url(#ring-core)" stroke-width="8"/>

    <g class="node-task">
      <circle cx="372" cy="250" r="117" fill="url(#node-task)" filter="url(#soft-shadow)"/>
      <circle cx="372" cy="250" r="94" fill="#fff"/>
      <circle cx="372" cy="250" r="82" fill="none" stroke="url(#node-task)" stroke-width="4"/>
      <g fill="none" stroke="#d8317e" stroke-width="1.6">
        <path d="M352 248 h40 M356 247 v-8 M362 247 v-12 M368 247 v-14 M374 247 v-18 M380 247 v-22 M386 247 v-26"/>
        <circle cx="384" cy="216" r="8"/>
      </g>
      <text class="label" x="372" y="283" font-size="25" text-anchor="middle">TASK</text>
    </g>

    <g class="node-individual">
      <circle cx="820" cy="510" r="165" fill="url(#node-individual)" filter="url(#soft-shadow)"/>
      <circle cx="820" cy="510" r="132" fill="#fff"/>
      <circle cx="820" cy="510" r="118" fill="none" stroke="url(#node-individual)" stroke-width="5"/>
      <g fill="none" stroke="#e8584f" stroke-width="2">
        <circle cx="820" cy="470" r="15"/>
        <circle cx="820" cy="465" r="5"/>
        <path d="M811 481 q9 -9 18 0"/>
        <path d="M820 450 v-12 M840 470 h12 M800 470 h-12 M834 456 l9 -9 M806 456 l-9 -9 M834 484 l9 9 M806 484 l-9 9"/>
      </g>
      <text class="label" x="823" y="554" font-size="31" text-anchor="middle">INDIVIDUAL</text>
    </g>

    <g class="node-team">
      <circle cx="340" cy="636" r="145" fill="url(#node-team)" filter="url(#soft-shadow)"/>
      <circle cx="340" cy="636" r="116" fill="#fff"/>
      <circle cx="340" cy="636" r="103" fill="none" stroke="url(#node-team)" stroke-width="4"/>
      <g fill="none" stroke="#d8317e" stroke-width="1.8">
        <path d="M340 583 l25 14 v29 l-25 14 l-25 -14 v-29 Z"/>
        <circle cx="340" cy="603" r="6"/>
        <path d="M330 620 q10 -12 20 0"/>
        <path d="M332 629 h16"/>
      </g>
      <text class="label" x="340" y="687" font-size="33" text-anchor="middle">TEAM</text>
    </g>
  </g>

  <!-- Panel 2: Seller maturity quadrant -->
  <g class="panel-quadrant">
    <rect x="62" y="907" width="1025" height="476" fill="var(--panel)"/>
    <circle cx="550" cy="1135" r="134" fill="url(#hub-fill)" filter="url(#wide-shadow)"/>
    <g filter="url(#soft-shadow)" fill="#fff">
      <path d="M423 998 a66 66 0 0 1 0 128 l-4 -18 a48 48 0 0 0 0 -92 Z"/>
      <path d="M677 998 a66 66 0 0 0 0 128 l4 -18 a48 48 0 0 1 0 -92 Z"/>
      <path d="M423 1158 a66 66 0 0 1 0 128 l-4 -18 a48 48 0 0 0 0 -92 Z"/>
      <path d="M677 1158 a66 66 0 0 0 0 128 l4 -18 a48 48 0 0 1 0 -92 Z"/>
    </g>
    <circle cx="405" cy="1062" r="46" fill="url(#disc-magenta)"/>
    <circle cx="695" cy="1062" r="46" fill="url(#disc-violet)"/>
    <circle cx="405" cy="1222" r="46" fill="url(#disc-blue)"/>
    <circle cx="695" cy="1222" r="46" fill="url(#disc-cyan)"/>
    <g class="icon">
      <circle cx="409" cy="1066" r="15"/><path d="M409 1056 v10 l6 5 M405 1049 h8 M384 1062 h10 M386 1068 h8"/>
      <circle cx="695" cy="1062" r="8"/><path d="M695 1040 v12 M695 1072 v12 M673 1062 h12 M705 1062 h12 M680 1047 l8 8 M702 1069 l8 8 M710 1047 l-8 8 M688 1069 l-8 8"/>
      <rect x="388" y="1206" width="34" height="26" rx="3"/><path d="M400 1232 v8 h12 M403 1213 l7 6 l-7 6 Z"/>
    </g>
    <g fill="none" stroke="#000" stroke-width="2.5">
      <circle cx="695" cy="1222" r="22"/><path d="M680 1230 l30 -20"/>
    </g>
    <text class="label" x="115" y="1073" font-size="25">ORDER TAKER</text>
    <text class="label" x="770" y="1055" font-size="25">TRANSACTIONAL</text>
    <text class="label" x="770" y="1091" font-size="25">TRADER</text>
    <text class="label" x="115" y="1210" font-size="25">SOLUTIONS</text>
    <text class="label" x="115" y="1250" font-size="25">PROVIDER</text>
    <text class="label" x="770" y="1235" font-size="25">TRUSTED ADVISOR</text>
  </g>

  <!-- Panel 3: Call structure -->
  <g class="panel-process">
    <rect x="62" y="1451" width="1025" height="460" fill="var(--panel)"/>
    <g filter="url(#soft-shadow)" fill="#fff">
      <path d="M130 1600 a75 75 0 0 1 148 0 l-18 4 a57 57 0 0 0 -112 0 Z"/>
      <path d="M382 1684 a75 75 0 0 0 148 0 l-18 -4 a57 57 0 0 1 -112 0 Z"/>
      <path d="M606 1600 a75 75 0 0 1 148 0 l-18 4 a57 57 0 0 0 -112 0 Z"/>
      <path d="M856 1684 a75 75 0 0 0 148 0 l-18 -4 a57 57 0 0 1 -112 0 Z"/>
    </g>
    <circle cx="204" cy="1625" r="56" fill="url(#disc-magenta)"/>
    <circle cx="455" cy="1660" r="56" fill="url(#disc-magenta)"/>
    <circle cx="680" cy="1625" r="56" fill="url(#disc-magenta)"/>
    <circle cx="930" cy="1660" r="56" fill="url(#disc-magenta)"/>
    <g class="icon">
      <circle cx="208" cy="1628" r="17"/><path d="M208 1617 v11 l7 6 M203 1607 h10 M178 1624 h12 M180 1632 h10 M183 1640 h10"/>
      <circle cx="455" cy="1655" r="13"/><path d="M464 1664 l14 14 M437 1642 q-6 -8 -14 0 M473 1642 q6 -8 14 0"/><circle cx="440" cy="1632" r="5"/><circle cx="470" cy="1632" r="5"/>
      <circle cx="680" cy="1625" r="24"/><circle cx="680" cy="1625" r="13"/><path d="M674 1625 l4 4 l8 -8"/>
      <path d="M908 1682 h44 M912 1682 v-24 h14 v24 M930 1682 v-30 h16 v30 M916 1664 h6 M916 1672 h6 M934 1660 h8 M934 1670 h8"/>
    </g>
    <path class="arrow" d="M298 1620 q0 42 68 20"/><path class="arrow" d="M354 1632 l14 6 l-4 14"/>
    <path class="arrow" d="M538 1632 q0 -40 64 -10"/><path class="arrow" d="M596 1610 l8 14 l-14 4"/>
    <path class="arrow" d="M774 1620 q0 42 68 20"/><path class="arrow" d="M830 1632 l14 6 l-4 14"/>
    <text class="label" x="458" y="1565" font-size="31" text-anchor="middle">RECRUIT</text>
    <text class="label" x="932" y="1565" font-size="31" text-anchor="middle">SUSTAIN</text>
    <text class="label" x="202" y="1745" font-size="31" text-anchor="middle">PLAN</text>
    <text class="label" x="676" y="1745" font-size="31" text-anchor="middle">EXECUTE</text>
    <text class="label" x="581" y="1827" font-size="18.5" text-anchor="middle">THIS IS HOW WE STRUCTURE OUR CALLS</text>
  </g>

  <!-- Panel 4: Call preparation checklist -->
  <g class="panel-checklist">
    <rect x="62" y="1972" width="1025" height="536" fill="var(--panel)"/>
    <g filter="url(#wide-shadow)">
      <rect x="406" y="2020" width="92" height="440" fill="#fff"/>
      <rect x="527" y="2020" width="92" height="440" fill="#fff"/>
      <rect x="649" y="2020" width="92" height="440" fill="#fff"/>
    </g>
    <path d="M406 2020 h92 v388 q-46 -40 -92 0 Z" fill="var(--violet)"/>
    <path d="M527 2020 h92 v388 q-46 -40 -92 0 Z" fill="var(--blue)"/>
    <path d="M649 2020 h92 v388 q-46 -40 -92 0 Z" fill="var(--navy)"/>
    <text class="bar-text" transform="translate(464 2356) rotate(-90)">Questions to ask?</text>
    <text class="bar-text" transform="translate(584 2370) rotate(-90)">Solutions to Needs?</text>
    <text class="bar-text" transform="translate(704 2368) rotate(-90)">Objections to Overcome?</text>
    <text class="label" x="452" y="2437" font-size="27" text-anchor="middle" style="fill:var(--violet)">01</text>
    <text class="label" x="575" y="2437" font-size="27" text-anchor="middle" style="fill:var(--blue)">02</text>
    <text class="label" x="697" y="2437" font-size="27" text-anchor="middle" style="fill:var(--navy)">03</text>
  </g>
</svg>
</div>
</body>
</html>
```